Bright Harbour - website for leadership service

I would like help to use a Squarespace template for a simple website.
We already have a logo which will influence the colour choice and tone.
Clean lines for executive audience. it is an exclusive service. I have all the content ready to go.
Would like some images included.

I will upload the content soon.

Does NOT need SEO as it will be direct mailed. Also does NOT need to consider having any payment pages or enquiry form.
Thanks

Target Market(s)

Women executives - senior leaders. Stylish, serious and capable.

Coding

Coded - Design and coding required

Number of Pages Required

3 page

Colors
3176b5
fee18a

Requirements
Must have
• Sqaurespace template. And scrolling down page format.

To suit style of the blue and gold logo.
Nice to have
• Simple, Stylish and exclusive feel. Inspiring but not "New Age"
Should not have
• Too many colours.

No

```html
<!DOCTYPE html>
<html lang="en">
<head>
<meta charset="utf-8">
<title>Bright Harbour</title>
<link href="https://fonts.googleapis.com/css2?family=Playfair+Display:ital,wght@0,400;0,700;1,700&display=swap" rel="stylesheet">
<style>
:root{
  --navy:#1b2641;
  --navy-deep:#161f36;
  --gold:#fede8a;
  --gold-text:#f6d27a;
  --body:#4a4a4a;
  --white:#ffffff;
  --dots-light:#fbf0d2;
  --dots-dark:#2b3652;
}
*{margin:0;padding:0;box-sizing:border-box}
html,body{width:1200px;height:3411px;overflow:hidden}
body{position:relative;background:var(--white);font-family:"Playfair Display",Georgia,serif;color:var(--body)}
.abs{position:absolute}
.site-header{left:0;top:0;width:1200px;height:99px;background:var(--navy);border-bottom:2px solid var(--gold)}
.brand{left:112px;top:32px;display:flex;align-items:center;gap:10px;color:var(--white);font-size:20px;letter-spacing:1px}
.brand-dot{width:14px;height:14px;border-radius:50%;background:var(--gold)}
.main-nav{left:645px;top:38px;display:flex;gap:31px;font-size:16px;color:var(--white)}
.main-nav .active{color:var(--gold-text)}
.hero-photo{left:0;top:100px;width:1200px;height:427px;background:linear-gradient(90deg,#f3d68a,#d9c4a6 30%,#fede8a 60%,#e9d2a0)}
.hero-band{left:0;top:527px;width:1200px;height:270px;background:var(--navy)}
.hero-dots{left:1033px;top:437px;width:126px;height:265px;background:var(--dots-dark)}
.hero-card{left:581px;top:331px;width:506px;height:297px;background:var(--gold);padding:28px 36px;color:var(--navy);font-size:28.5px;line-height:33px}
.hero-card em{font-weight:700}
.hero-lead{left:94px;top:570px;width:480px;color:var(--white);font-weight:700;font-size:27px;line-height:39px}
.hero-sub{left:94px;top:666px;width:1000px;color:var(--white);font-weight:700;font-size:27px;line-height:39px}
.gold-block{background:var(--gold)}
.photo{background:linear-gradient(135deg,#3a2a26,#b4614a 55%,#e7a36f)}
.photo-crowd{background:linear-gradient(160deg,#c98a52,#5a3a2c 55%,#2a211e)}
.photo-audience{background:linear-gradient(140deg,#6a4a3c,#b0876a 50%,#3c2e2a)}
.dots{background:var(--dots-light)}
h2{font-weight:700;color:var(--navy);font-size:28px;line-height:33px}
.copy p{font-size:18.5px;line-height:22.5px;margin-bottom:22px}
.ticks{list-style:none}
.ticks li{font-size:18.5px;line-height:22.5px;margin-bottom:22px;padding-left:27px;position:relative}
.ticks li::before{content:">";position:absolute;left:0}
.site-footer{left:0;top:3064px;width:1200px;height:258px;background:var(--navy)}
.footer-brand{left:94px;top:3160px;color:var(--white);font-size:22px;letter-spacing:2px;display:flex;align-items:center;gap:12px}
.footer-brand .brand-dot{width:18px;height:18px}
.footer-title{color:var(--gold-text);font-weight:700;font-size:20px}
.footer-links{list-style:none;color:var(--white);font-size:16px;line-height:27px}
.social{display:flex;gap:12px}
.social span{width:36px;height:36px;border-radius:50%;background:var(--white);display:block}
.copyright-bar{left:0;top:3322px;width:1200px;height:89px;background:var(--navy-deep);color:#c9ccd4;font-size:16px;text-align:center;line-height:89px}
</style>
</head>
<body>
<header class="abs site-header">
  <div class="abs brand"><span class="brand-dot"></span>Bright Harbour</div>
  <nav class="abs main-nav"><span class="active">Home</span><span>About</span><span>Testimonials</span><span>Resources</span><span>Contact</span></nav>
</header>

<div class="abs hero-photo" role="img" aria-label="Group of smiling businesswomen standing with arms crossed against a gold backdrop"></div>
<div class="abs hero-band"></div>
<div class="abs hero-dots" role="img" aria-label="Faint dot grid decoration"></div>
<div class="abs hero-card"><em>BRIGHT HARBOUR</em> is a premier leadership coaching service entirely focused on supporting women in executive roles to lead commercially successful businesses in ways that align with their core values and principles.</div>
<p class="abs hero-lead">A new era of values-driven business has begun, led by women like you:</p>
<p class="abs hero-sub">capable, proven leaders who are challenging the status quo and redefining the meaning of business success</p>

<section>
  <div class="abs dots" style="left:66px;top:1192px;width:126px;height:261px" role="img" aria-label="Faint dot grid decoration"></div>
  <div class="abs gold-block" style="left:94px;top:857px;width:366px;height:536px"></div>
  <div class="abs photo" style="left:150px;top:907px;width:450px;height:451px" role="img" aria-label="Woman speaking at a lectern before a blurred conference audience"></div>
  <h2 class="abs" style="left:646px;top:873px">What is BRIGHT HARBOUR?</h2>
  <div class="abs copy" style="left:649px;top:944px;width:450px">
    <p>Women are at the forefront of a global movement of leaders pioneering new business models. BRIGHT HARBOUR will connect you to this movement and get you excited about business leadership again.</p>
    <p>What made business successful in the past is not working. Long established traditions of politicking, closed door decision making and a constant focus on short-term quick wins and shareholder profit are no longer a guarantee of good business results.</p>
    <p>To be successful, businesses must deliver as much value for employees, customers, suppliers and wider communities, as they do for shareholders.</p>
    <p>This isn’t a nice to have, it is a MUST have for commercial success.</p>
  </div>
</section>

<section>
  <h2 class="abs" style="left:69px;top:1512px;width:460px">Is it time for me to be a part of BRIGHT HARBOUR?</h2>
  <div class="abs copy" style="left:68px;top:1608px;width:520px">
    <p>You are already successful, but you may be questioning whether you want to put your hand up for bigger roles. That is entirely understandable with the current business focus on short-term profit and unsustainable demands on people.</p>
    <p>You may feel isolated in busy, demanding roles. You would love to have other women to connect who share the same values. You don’t have space for networking and have wasted too much time in leadership programmes that would have you fitting into old ways of doing things.</p>
    <p>You may get frustrated by old thinking and believe there is a better way of doing things. You are deeply committed to making a difference in the world and want to work on what matters most. You are serious about ways to:</p>
    <ul class="ticks">
      <li>Ensure long-term, ethical business success</li>
      <li>Find ways to bring purpose front and centre</li>
      <li>Transform organisations to respect people, employees and the communities the business serves</li>
      <li>Reprioritise learning, wellbeing, rest and renewal.</li>
    </ul>
  </div>
  <div class="abs dots" style="left:702px;top:2046px;width:128px;height:122px" role="img" aria-label="Faint dot grid decoration"></div>
  <div class="abs gold-block" style="left:762px;top:1511px;width:365px;height:604px"></div>
  <div class="abs photo-crowd" style="left:629px;top:1592px;width:450px;height:449px" role="img" aria-label="Large blurred crowd in a warmly lit auditorium"></div>
</section>

<section>
  <div class="abs dots" style="left:391px;top:2768px;width:126px;height:219px" role="img" aria-label="Faint dot grid decoration"></div>
  <div class="abs gold-block" style="left:73px;top:2261px;width:365px;height:644px"></div>
  <div class="abs photo-audience" style="left:128px;top:2311px;width:451px;height:451px" role="img" aria-label="Applauding audience at a business event"></div>
  <h2 class="abs" style="left:629px;top:2266px">How will BRIGHT HARBOUR help me?</h2>
  <div class="abs copy" style="left:629px;top:2337px;width:515px">
    <p>No one understands as well as you, the blocks and challenges of working in current business models. BRIGHT HARBOUR will strengthen your leadership with new thinking, new models and the ability to tap into your own deep wisdom.</p>
    <p>&gt; Navigate current business challenges without compromising your values.</p>
    <p>&gt; Find ways to deliver hard commercial imperatives with grace and ethical integrity.</p>
    <p>&gt; Get extra support to effectively challenge outdated ways of thinking and influence better ways of leading.</p>
    <p>&gt; Stand strong during the inevitable lows of leadership, get support when things get tough, and protect what’s most important: your family, your health and wellbeing, and your sense of self.</p>
    <p>&gt; Clean up negative patterns and habits in a high-trust setting. This is a deep process and one that needs an experienced guide.</p>
    <p>&gt; Get a curated synthesis of the latest thinking from leaders around the world. You can relax knowing that you can have your finger on the pulse of the new thinking and approaches.</p>
  </div>
</section>

<footer>
  <div class="abs site-footer"></div>
  <div class="abs footer-brand"><span class="brand-dot"></span>Harbour Light Coaching</div>
  <p class="abs footer-title" style="left:555px;top:3126px">Overview</p>
  <ul class="abs footer-links" style="left:555px;top:3172px">
    <li>About Us</li><li>Testimonials</li><li>Resources</li><li>Contact</li>
  </ul>
  <p class="abs footer-title" style="left:850px;top:3132px">Join our social media</p>
  <div class="abs social" style="left:893px;top:3191px" aria-label="Social media links"><span></span><span></span><span></span></div>
  <div class="abs copyright-bar">© Copyright 2020 BRIGHT HARBOUR. All Rights Reserved</div>
</footer>
</body>
</html>
```